Private Villa in Bali looking for a flyer design

We need a flyer design for a 2bedrooms private villa with pool in Bali, called VILLA SEKAR

Our villa is a private 2 bedrooms villa with private swimming pool, tranquil , luxurious, blending balinese and modern interiors , personal service and family home away from home
Out Motto : your blissful getaway

We would like an elegant, luxury and clean design

Colour scheme : BROWN, YELLOW/GOLD, GREY

It should have :
1/photo of the villa
2/ basic info of the villa
3/ location/address and location map of the villa

Villa Sekar
Banjar Tegalsari,
Kelodayu, Sumbawi
Bali - Indonesia

4/ website :
www.villasekarbintang

5/ email :
wulan@villasekarbintang.com

6/ Phone :
+852-57204916

I have attached some photos and the logo, please let me know if you need ai/eps file

Thank you . Please let me know if you need more information
Updates

-Trifold flyer on A4 size paper ( standard size flyer)

-Front page : Main photo and Logo
-Last page : Location map, email,website etc
-Page 2-4 : any design with photo and info from website 

Target Market(s)

Family, couples, honeymooners

Industry/Entity Type

It Service

Colors
ffc214
474747
9d9d9d

Requirements
Must have
• address, location map, website and email add, photos ( don't need to use all)

Trifold on A4 size paper double sided
Nice to have
• Trifold on A4 size paper
Should not have
• too many photos overlapping .

```html
<!DOCTYPE html>
<html lang="en">
<head>
<meta charset="utf-8">
<title>Villa Sekar — Trifold Flyer</title>
<link href="https://fonts.googleapis.com/css2?family=Quicksand:wght@400;500;600&family=Open+Sans:wght@400;600&family=Caveat:wght@500&display=swap" rel="stylesheet">
<style>
  :root {
    --brown-dark: #3f2b19;
    --brown: #5a3f24;
    --brown-mid: #6b4e31;
    --beige: #e6ddcf;
    --beige-light: #f1ebe1;
    --gold: #ffc214;
    --ink: #474747;
    --grey: #9d9d9d;
    --paper-bg: #d9d9d9;
    --text-light: #f3ece0;
    --text-muted: #8a7a66;
  }
  * { margin: 0; padding: 0; box-sizing: border-box; }
  html, body { width: 1200px; height: 863px; overflow: hidden; }
  body {
    background: radial-gradient(ellipse at 50% 35%, #f2f2f2 0%, var(--paper-bg) 100%);
    font-family: "Quicksand", sans-serif;
    position: relative;
  }
  .sheet {
    position: absolute;
    top: 220px;
    width: 560px;
    height: 396px;
    display: flex;
    box-shadow: 0 10px 24px rgba(0,0,0,0.22);
    background: var(--beige);
  }
  .sheet--inside { left: 25px; }
  .sheet--front { left: 615px; }
  .sheet-label {
    position: absolute;
    top: 634px;
    width: 560px;
    text-align: center;
    font-family: "Open Sans", sans-serif;
    font-size: 19px;
    color: #222;
  }
  .sheet-label--inside { left: 25px; }
  .sheet-label--front { left: 615px; }

  .panel { position: relative; width: 186.67px; height: 100%; overflow: hidden; }
  .photo { position: absolute; left: 0; right: 0; }

  /* FRONT: interior panel */
  .photo--living {
    top: 0; bottom: 0;
    background: linear-gradient(180deg, #6b3d1c 0%, #b9834e 22%, #e8cfa0 45%, #7a5638 72%, #3a2a22 100%);
  }

  /* FRONT: info + contact panel */
  .info { position: absolute; top: 0; left: 0; right: 0; height: 222px; background: var(--beige); padding: 18px 10px 0; }
  .info__title {
    text-align: center; font-weight: 500; font-size: 15px; line-height: 1.15;
    letter-spacing: 0.5px; color: var(--brown-mid); margin-bottom: 12px;
  }
  .info__body { font-size: 5.6px; line-height: 1.55; color: var(--text-muted); text-align: justify; }
  .info__body p + p { margin-top: 6px; }
  .contact {
    position: absolute; top: 222px; left: 0; right: 0; height: 100px;
    background: var(--brown-dark); color: var(--text-light); text-align: center; padding-top: 10px;
  }
  .contact__title { font-size: 12px; font-weight: 500; letter-spacing: 1px; margin-bottom: 6px; }
  .contact__line { font-size: 5.2px; line-height: 1.6; letter-spacing: 0.3px; }
  .contact__line--gap { margin-top: 4px; }
  .map {
    position: absolute; top: 322px; bottom: 0; left: 0; right: 0;
    background: linear-gradient(160deg, #e9e9e9 0%, #d6d6d6 60%, #b9cfe0 100%);
  }
  .map__pin { position: absolute; left: 86px; top: 26px; }

  /* FRONT: cover panel */
  .photo--pool {
    top: 0; height: 132px;
    background: linear-gradient(180deg, #5b79b8 0%, #8a9ab4 35%, #4a3a3a 62%, #2fa6e0 78%, #1a8ed0 100%);
  }
  .cover { position: absolute; top: 132px; bottom: 0; left: 0; right: 0; background: var(--brown); text-align: center; }
  .brand { margin-top: 26px; display: flex; flex-direction: column; align-items: center; gap: 14px; }
  .brand__mark { width: 48px; height: 48px; background: var(--gold); }
  .brand__name { font-family: "Quicksand", sans-serif; font-weight: 500; font-size: 24px; color: var(--gold); letter-spacing: 0.5px; }
  .motto { margin-top: 30px; font-family: "Caveat", cursive; font-size: 17px; color: var(--text-light); }

  /* INSIDE: food panel */
  .food-head { position: absolute; top: 0; left: 0; right: 0; height: 66px; background: var(--brown-mid); color: var(--text-light); text-align: center; padding-top: 12px; }
  .food-head__title { font-size: 9px; letter-spacing: 1.5px; font-weight: 500; margin-bottom: 6px; }
  .food-head__text { font-size: 5px; line-height: 1.5; padding: 0 34px; }
  .photo--dining { top: 66px; height: 176px; background: linear-gradient(135deg, #c2362a 0%, #d9b36a 40%, #6e4326 75%, #3a2518 100%); }
  .food { position: absolute; top: 242px; bottom: 0; left: 0; right: 0; background: var(--beige-light); padding: 16px 14px 0; text-align: center; }
  .section-title { font-size: 11px; letter-spacing: 1.5px; font-weight: 500; color: var(--brown-mid); margin-bottom: 5px; }
  .section-lead { font-size: 5.6px; line-height: 1.5; color: var(--text-muted); margin-bottom: 6px; }
  .section-body { font-size: 5px; line-height: 1.6; color: var(--grey); }

  /* INSIDE: services + rooms (two panels sharing bottom photo) */
  .spread { position: relative; width: 373.33px; height: 100%; }
  .services-top { position: absolute; top: 0; left: 0; width: 186.67px; height: 60px; background: var(--beige-light); }
  .services-band { position: absolute; top: 60px; left: 0; width: 186.67px; height: 130px; background: var(--brown); color: var(--text-light); text-align: center; padding-top: 30px; }
  .services-band__title { font-size: 12px; letter-spacing: 2px; font-weight: 500; }
  .services-band__rule { width: 130px; height: 1px; background: var(--text-light); opacity: 0.6; margin: 10px auto 0; }
  .photo--suite { top: 0; left: 186.67px; width: 186.67px; height: 84px; background: linear-gradient(135deg, #3a2418 0%, #a9653a 45%, #e9c89b 100%); }
  .rooms { position: absolute; top: 84px; left: 186.67px; width: 186.67px; height: 106px; background: var(--beige-light); padding: 14px 16px 0; text-align: center; }
  .photo--bedroom { top: 190px; left: 0; width: 373.33px; bottom: 0; background: linear-gradient(120deg, #2e2520 0%, #7a6452 30%, #d8c7b0 55%, #8a1f1c 75%, #4f7a3a 100%); }
  .caption { position: absolute; right: 14px; top: 300px; width: 118px; background: var(--brown-dark); color: var(--text-light); font-size: 5px; line-height: 1.5; padding: 6px 8px; }
</style>
</head>
<body>

  <!-- Inside spread -->
  <section class="sheet sheet--inside" aria-label="Inside of trifold">
    <div class="panel">
      <div class="food-head">
        <h3 class="food-head__title">HARCIMUS ET ABOR</h3>
        <p class="food-head__text">The variety of traditional and Mediterranean food with quality and tasty dishes.</p>
      </div>
      <div class="photo photo--dining" role="img" aria-label="Photo of the dining room with a set table and red walls"></div>
      <div class="food">
        <h3 class="section-title">FOOD</h3>
        <p class="section-lead">Quiet and Comfortable, rooms are in categories, Single, Double, Triple and Quadruple.</p>
        <p class="section-body">Breakfast is served at the table each morning, with fresh fruit, local coffee and dishes made to order by our cook from the village market.</p>
      </div>
    </div>
    <div class="spread">
      <div class="services-top"></div>
      <div class="services-band">
        <h3 class="services-band__title">SERVICIES</h3>
        <div class="services-band__rule"></div>
      </div>
      <div class="photo photo--suite" role="img" aria-label="Photo of the lounge with wooden ceiling and sofas"></div>
      <div class="rooms">
        <h3 class="section-title">ROOMS</h3>
        <p class="section-lead">Quiet and Comfortable, rooms are in categories, Single, Double, Triple and Quadruple.</p>
        <p class="section-body">Generous rooms open onto shaded terraces and the garden pool, each with soft linen, carved teak furniture, cool air and quiet corners for slow mornings and long afternoons.</p>
      </div>
      <div class="photo photo--bedroom" role="img" aria-label="Photo of the bedroom opening onto the garden through glass doors"></div>
      <p class="caption">Doors open wide to the pool deck, letting in light and the scent of frangipani.</p>
    </div>
  </section>
  <p class="sheet-label sheet-label--inside">inside</p>

  <!-- Front (outside) spread -->
  <section class="sheet sheet--front" aria-label="Outside of trifold">
    <div class="panel">
      <div class="photo photo--living" role="img" aria-label="Photo of the high-ceilinged living and dining area with open kitchen"></div>
    </div>
    <div class="panel">
      <div class="info">
        <h2 class="info__title">VILLA SEKAR<br>SUMBAWI, BALI</h2>
        <div class="info__body">
          <p>Since the beginning of time Bali has been known as the 'Island of the Gods', a mystical and beautiful place that has captured the hearts and imaginations of all who lay eyes on her. Away from the hustle and bustle of the modern world, yet close enough to the conveniences that make life comfortable, Villa Sekar is nestled in the charming Balinese village of Kelodayu, Sumbawi. Gentle rolling valleys stepped with rice paddies provide the perfect backdrop for those looking for picture postcard views of Bali and the beautiful Batu Mejan Beach.</p>
          <p>Villa Sekar is within easy reach of Bali's great shopping and nightlife of Legian Kaja &amp; the Taman Sari golf course designed by a champion golfer.</p>
        </div>
      </div>
      <div class="contact">
        <h3 class="contact__title">CONTACT</h3>
        <p class="contact__line">BANJAR TEGALSARI,<br>KELODAYU, SUMBAWI BALI - INDONESIA</p>
        <p class="contact__line contact__line--gap">CALL : +852-57204916</p>
        <p class="contact__line contact__line--gap">E-mail: wulan@villasekarbintang.com<br>Web Site: www.villasekarbintang</p>
      </div>
      <div class="map" role="img" aria-label="Location map of the villa near the coast">
        <svg class="map__pin" width="10" height="14" viewBox="0 0 10 14" aria-hidden="true">
          <path d="M5 0a5 5 0 0 0-5 5c0 3.5 5 9 5 9s5-5.5 5-9a5 5 0 0 0-5-5z" fill="#3a5fa8"/>
          <circle cx="5" cy="5" r="2" fill="#ffffff"/>
        </svg>
      </div>
    </div>
    <div class="panel">
      <div class="photo photo--pool" role="img" aria-label="Photo of the villa with its blue swimming pool at dusk"></div>
      <div class="cover">
        <div class="brand">
          <div class="brand__mark"></div>
          <span class="brand__name">Villa Sekar</span>
        </div>
        <p class="motto">your blissful getaway</p>
      </div>
    </div>
  </section>
  <p class="sheet-label sheet-label--front">front</p>

</body>
</html>
```